Broschüre für Energieberater
Zielgruppe
Unternehmen die zu den KMU´s gehören (kleine und mittlere Unternehmen) haben die Möglichkeit eine Energieberatung über die ZEKV fördern zu lassen. Diese Beratung wird durch unsere Ingenieure durchgeführt und ist für den Kunden völlig kostenneutral. Zum einen erhält er eine 80% Förderung von der ZEKV (Zentralstelle für Kostenausgleich und Versorgung) die restlichen 20% erhält der Kunde von uns als Gutschrift. Wir finanzieren uns somit nur über die Fördergelder des Bundes. Die Vorteile des Kunden sind: Verringerung von Steuern, Einsparung von mindestens 10% an Energie ohne zusätzliche Kosten und somit weniger C0² Ausstoss, was wiederum allen zugute kommt. Somit ein hohes Maß an Umweltbewusstsein! Alle Investitionen die für die Einsparung von Energie von Vorteil sind, werden vom Bund mit bis zu 200.000 Euro gefördert. Voraussetzung eine durchgeführte ZEKV Energieberatung. Somit eine win/win Situation für alle Beteiligten.
Aufgabenstellung
Das Design kann - muss - nicht an unsere Webseite : www.wattlinde-beratung.de angelehnt sein.

```html
<!DOCTYPE html>
<html lang="de">
<head>
<meta charset="utf-8">
<title>Broschüre Energieberatung – Innenseite</title>
<link rel="stylesheet" href="https://fonts.googleapis.com/css2?family=Kalam:wght@700&family=Arimo:wght@400;700&display=swap">
<style>
  :root {
    --page-bg: #d6d6d6;
    --paper: #ececec;
    --ink: #3f3f42;
    --placeholder-a: #dcdcdc;
    --placeholder-b: #cfd6db;
  }
  * { box-sizing: border-box; margin: 0; padding: 0; }
  html, body { width: 1200px; height: 1200px; overflow: hidden; }
  body { background: var(--page-bg); font-family: "Arimo", Arial, sans-serif; color: var(--ink); }

  .spread {
    position: absolute; left: 30px; top: 190px;
    width: 1140px; height: 820px;
    background: var(--paper);
    box-shadow: 0 10px 30px rgba(0,0,0,0.18);
    overflow: hidden;
  }
  .header-band { position: absolute; left: 0; top: 0; width: 1140px; height: 260px; }
  .fold { position: absolute; top: 0; bottom: 0; width: 1px; background: rgba(0,0,0,0.08); }
  .fold--one { left: 380px; }
  .fold--two { left: 760px; }

  .panel { position: absolute; top: 0; width: 380px; height: 820px; }
  .panel--costs { left: 0; }
  .panel--savings { left: 380px; }
  .panel--experts { left: 760px; }

  .heading {
    position: absolute;
    font-family: "Kalam", "Comic Sans MS", cursive;
    font-weight: 700; color: var(--ink);
    font-size: 30px; line-height: 43px; letter-spacing: 0.3px;
    text-transform: uppercase; white-space: nowrap;
  }
  .subheading {
    position: absolute;
    font-family: "Kalam", "Comic Sans MS", cursive;
    font-weight: 700; color: var(--ink);
    font-size: 23px; line-height: 36px;
    text-transform: uppercase; white-space: nowrap;
  }
  .body-copy {
    position: absolute;
    font-size: 15px; line-height: 24px; font-weight: 700;
    color: var(--ink);
  }
  .illustration {
    position: absolute; border-radius: 14px;
    background: linear-gradient(135deg, var(--placeholder-a), var(--placeholder-b));
  }

  .panel--costs .coin { left: 0; top: 32px; width: 110px; height: 140px; }
  .panel--costs .heading { left: 142px; top: 30px; }
  .panel--costs .intro { left: 40px; top: 290px; width: 320px; }
  .panel--costs .subheading { left: 40px; top: 512px; }
  .panel--costs .funding { left: 40px; top: 600px; width: 320px; }

  .panel--savings .heading { left: 32px; top: 30px; }
  .panel--savings .bulb { left: 150px; top: 138px; width: 140px; height: 195px; }
  .panel--savings .copy { left: 32px; top: 380px; width: 320px; }

  .panel--experts .heading { left: 36px; top: 30px; }
  .panel--experts .copy { left: 36px; top: 290px; width: 320px; }
  .panel--experts .team { left: 95px; top: 570px; width: 230px; height: 190px; }
</style>
</head>
<body>
  <main class="spread">
    <svg class="header-band" viewBox="0 0 1140 260" aria-hidden="true">
      <defs>
        <linearGradient id="bandFill" x1="0" y1="0" x2="1" y2="0">
          <stop offset="0" stop-color="#3b85b7"/>
          <stop offset="0.33" stop-color="#3f8cbf"/>
          <stop offset="0.335" stop-color="#5aaad3"/>
          <stop offset="0.66" stop-color="#66b3da"/>
          <stop offset="0.665" stop-color="#6fbbdf"/>
          <stop offset="1" stop-color="#7dc4e4"/>
        </linearGradient>
      </defs>
      <polygon points="0,0 1140,0 1140,172 0,258" fill="url(#bandFill)"/>
    </svg>
    <div class="fold fold--one"></div>
    <div class="fold fold--two"></div>

    <section class="panel panel--costs">
      <div class="illustration coin" role="img" aria-label="Platz für gezeichnete Münze mit Euro-Zeichen"></div>
      <h2 class="heading">Keine<br>versteckten<br>Kosten!</h2>
      <p class="body-copy intro">Deutschland ist beim Erreichen seiner Klimaziele nicht auf Kurs und will deshalb mit dem Fördern von Energieberatungen mittelständische deutsche Unternehmen motivieren, energiesparende Maßnahmen zu treffen. Die darin empfohlenen Umsetzungen sind freiwillig. Zu keinem Zeitpunkt entstehen Ihnen versteckte Kosten!</p>
      <h3 class="subheading">Staatliche Fördermittel<br>sichern!</h3>
      <p class="body-copy funding">Die Fördermittel sind aktuell gesichert, dies kann der Gesetzgeber jedoch jederzeit ändern. Fördermittel sollten daher genutzt werden, solange sie zur Verfügung stehen. Die Fördermittel werden von der Zentralstelle für Kostenausgleich und Versorgung bereitgestellt.</p>
    </section>

    <section class="panel panel--savings">
      <h2 class="heading">Bis zu 25% Energie<br>&amp; Kosten einsparen</h2>
      <div class="illustration bulb" role="img" aria-label="Platz für gezeichnete Glühbirne"></div>
      <p class="body-copy copy">Viele Unternehmer wurden bisher noch nicht ausreichend über ihren Energiehaushalt aufgeklärt. Ein auf Energieberatung spezialisierter Ingenieur erkennt schnell, an welchen Ecken mit wenig Aufwand viel Energie gespart werden kann. So wird langfristig nicht nur die Umwelt, sondern auch der eigene Geldbeutel geschont.</p>
    </section>

    <section class="panel panel--experts">
      <h2 class="heading">Von Experten<br>gesicherte<br>Durchführung</h2>
      <p class="body-copy copy">Wattlinde kann dank seiner langen Erfahrung in der Energiebranche eine problemlose Anmeldung garantieren. Alle Formulare müssen optimal ausgefüllt sein, um die Chancen auf eine maximale Förderung zu gewährleisten. Wenn die Zusage zur Förderung eintrifft, wird Wattlinde einen vom Staat zertifizierten Ingenieur zur Energieberatung vorbei schicken.</p>
      <div class="illustration team" role="img" aria-label="Platz für gezeichnete Figuren zweier Berater"></div>
    </section>
  </main>
</body>
</html>
```